New minimal and cool business card

We have a brand new logo - we would like to use the logo on blue on the front of the card
The tagline is The give and take network (tm)
We would like information on the back of the card for individual(s)

Our font is Lato
Our colors are indicated in the attached identity guide which uses the old logo - we are de-emphasizing orange

Please prepare the artwork to meet the specs on this site
http://us.prinvo.com/products/velora/business-cards.html

Front: Logo and tagline on dark blue

Back: On white
Join Today
http://zentaro.co/join

```html
<!DOCTYPE html>
<html lang="en">
<head>
<meta charset="utf-8">
<title>Zentaro Business Card</title>
<link rel="stylesheet" href="https://fonts.googleapis.com/css2?family=Lato:wght@300;400;700&display=swap">
<style>
  :root {
    --backdrop: #7d7a79;
    --brand-navy: #354a5f;
    --brand-orange: #f0901e;
    --paper: #ffffff;
  }
  * { margin: 0; padding: 0; box-sizing: border-box; }
  html, body {
    width: 1000px;
    height: 1200px;
    overflow: hidden;
    background: var(--backdrop);
    font-family: "Lato", sans-serif;
  }
  .sheet {
    position: relative;
    width: 1000px;
    height: 1200px;
  }
  .card {
    position: absolute;
    left: 77px;
    width: 828px;
    height: 543px;
  }
  .card--front {
    top: 35px;
    background: var(--brand-navy);
  }
  .card--back {
    top: 621px;
    background: var(--paper);
  }
  .wordmark {
    position: absolute;
    left: 0;
    right: 0;
    top: 220px;
    text-align: center;
    color: var(--paper);
    font-family: "Lato", sans-serif;
    font-weight: 400;
    font-size: 112px;
    line-height: 1;
    letter-spacing: 1px;
  }
  .cta {
    position: absolute;
    left: 0;
    right: 0;
    top: 188px;
    text-align: center;
    color: var(--brand-orange);
    font-family: "Lato", sans-serif;
    font-weight: 300;
    font-size: 96px;
    line-height: 1.2;
  }
  .url-band {
    position: absolute;
    left: 0;
    right: 0;
    top: 383px;
    height: 58px;
    background: var(--brand-navy);
    display: flex;
    align-items: center;
    justify-content: center;
  }
  .url {
    color: var(--paper);
    font-family: "Lato", sans-serif;
    font-weight: 300;
    font-size: 36px;
    line-height: 1;
    margin-left: -18px;
  }
</style>
</head>
<body>
  <main class="sheet">
    <section class="card card--front" aria-label="Card front">
      <div class="wordmark">zentaro</div>
    </section>
    <section class="card card--back" aria-label="Card back">
      <h1 class="cta">Join Today</h1>
      <div class="url-band">
        <span class="url">http://zentaro.co/join</span>
      </div>
    </section>
  </main>
</body>
</html>
```